Water Board Political Campaign Sign

1. Simple elegant clean design highly visible possibly with white text and blue and green as accent colors and water theme as design element
2. Clean sans-serif fonts like Helvetica or Arial
3. Wording on sign: Rick (small font) Darvell (largest font possible) & Patricia (small font) Crestani (largest font possible) but please do not use all caps for names.
for Marlow Brook Water District Directors (slightly smaller font)
Leading with Experience, Committed to a Sustainable Future
Vote Nov. 5 ( small font size)
In very small font at bottom of sign FPPC#2893164
4. We need two yard signs--one medium sign about 18" x 24" and
another larger sign about 48" x 96"

Target Market(s)

Mixed township 60% Democrat

Industry/Entity Type

Water

Font styles to use
Sans Serif

Requirements
Must have
• Water theme

```html
<!DOCTYPE html>
<html lang="en">
<head>
<meta charset="utf-8">
<title>Darvell &amp; Crestani – Yard Sign</title>
<link rel="stylesheet" href="https://fonts.googleapis.com/css2?family=Roboto+Condensed:wght@700;800&family=Arimo:wght@400&display=swap">
<style>
  :root {
    --backdrop: #bfbfbf;
    --sign-green: #8dc63f;
    --wave-deep: #2f8a2a;
    --wave-mid: #5fae34;
    --wave-light: #a9d86a;
    --ink-white: #ffffff;
  }
  html, body {
    margin: 0;
    padding: 0;
    width: 1200px;
    height: 1200px;
    overflow: hidden;
    background: var(--backdrop);
  }
  .yard-sign {
    position: absolute;
    left: 210px;
    top: 80px;
    width: 780px;
    height: 1039px;
    background: var(--sign-green);
    box-shadow: 4px 5px 8px rgba(0,0,0,0.3);
    overflow: hidden;
  }
  .water-band {
    position: absolute;
    left: 0;
    width: 780px;
  }
  .water-band--upper { top: 350px; height: 250px; }
  .water-band--lower { top: 830px; height: 190px; }
  .candidate-names {
    position: absolute;
    left: 0;
    top: 0;
    width: 780px;
    height: 560px;
  }
  .candidate-names .surname {
    font-family: "Roboto Condensed", "Arial Narrow", sans-serif;
    font-weight: 800;
    font-size: 172px;
    fill: var(--ink-white);
  }
  .candidate-names .given-name {
    font-family: "Roboto Condensed", "Arial Narrow", sans-serif;
    font-weight: 700;
    font-size: 42px;
    fill: var(--ink-white);
  }
  .sign-copy {
    position: absolute;
    left: 0;
    width: 780px;
    text-align: center;
    color: var(--ink-white);
    font-family: "Arimo", Arial, Helvetica, sans-serif;
    margin: 0;
    line-height: 1;
    white-space: nowrap;
  }
  .office-line { top: 612px; font-size: 28px; }
  .slogan-line { top: 672px; font-size: 24px; }
  .vote-date { top: 765px; font-size: 30px; }
  .fppc-id {
    position: absolute;
    right: 48px;
    top: 962px;
    margin: 0;
    color: var(--ink-white);
    font-family: "Arimo", Arial, Helvetica, sans-serif;
    font-size: 24px;
    line-height: 1;
  }
</style>
</head>
<body>
  <main class="yard-sign">
    <svg class="water-band water-band--upper" viewBox="0 0 780 250" role="img" aria-label="Translucent green water surface wave with small bubbles">
      <defs>
        <linearGradient id="upperWave" x1="0" y1="0" x2="0" y2="1">
          <stop offset="0" stop-color="var(--wave-deep)" stop-opacity="0.6"/>
          <stop offset="0.45" stop-color="var(--wave-mid)" stop-opacity="0.35"/>
          <stop offset="1" stop-color="var(--sign-green)" stop-opacity="0"/>
        </linearGradient>
      </defs>
      <path d="M0 10 C120 0 220 50 340 60 C460 70 560 105 660 125 C720 138 760 130 780 125 L780 250 L0 250 Z" fill="url(#upperWave)"/>
      <path d="M0 10 C120 0 220 50 340 60 C460 70 560 105 660 125 C720 138 760 130 780 125" fill="none" stroke="var(--wave-light)" stroke-width="3" opacity="0.7"/>
    </svg>
    <svg class="water-band water-band--lower" viewBox="0 0 780 190" role="img" aria-label="Translucent green water surface wave with small bubbles">
      <defs>
        <linearGradient id="lowerWave" x1="0" y1="0" x2="0" y2="1">
          <stop offset="0" stop-color="var(--wave-deep)" stop-opacity="0.6"/>
          <stop offset="0.5" stop-color="var(--wave-mid)" stop-opacity="0.3"/>
          <stop offset="1" stop-color="var(--sign-green)" stop-opacity="0"/>
        </linearGradient>
      </defs>
      <path d="M0 25 C140 20 260 40 360 30 C470 18 560 10 660 18 C720 22 760 28 780 30 L780 190 L0 190 Z" fill="url(#lowerWave)"/>
      <path d="M0 25 C140 20 260 40 360 30 C470 18 560 10 660 18 C720 22 760 28 780 30" fill="none" stroke="var(--wave-light)" stroke-width="3" opacity="0.7"/>
    </svg>

    <svg class="candidate-names" viewBox="0 0 780 560" aria-label="Rick Darvell and Patricia Crestani">
      <defs>
        <filter id="nameShadow" x="-5%" y="-5%" width="110%" height="120%">
          <feDropShadow dx="2" dy="3" stdDeviation="2" flood-color="#000" flood-opacity="0.35"/>
        </filter>
      </defs>
      <g filter="url(#nameShadow)">
        <text class="given-name" x="94" y="180">Rick</text>
        <text class="surname" x="90" y="330" textLength="598" lengthAdjust="spacingAndGlyphs">Darvell &amp;</text>
        <text class="given-name" x="94" y="388">Patricia</text>
        <text class="surname" x="90" y="530" textLength="598" lengthAdjust="spacingAndGlyphs">Crestani</text>
      </g>
    </svg>

    <p class="sign-copy office-line">for Marlow Brook Water District Directors</p>
    <p class="sign-copy slogan-line">Leading with Experience, Committed to a Sustainable Future</p>
    <p class="sign-copy vote-date">Vote Nov. 5</p>
    <p class="fppc-id">FPPC#2893164</p>
  </main>
</body>
</html>
```